Tarnwickhub.com home page

On the existing home page I want to eliminate people in circles and promote these three earning opportunities:
1." Make a referral to existing advertiser"
Earn up to $5000 when you make a successful referral to one of our advertisers.
2."Sign up a new business to offer referral commisions to ambassaadors". Earn up to $5000 or more when you earn 5% of money paid out by business in referral fees.
3."Sign up new ambassadors"
Earn up to $5000 or more when you earn 5% of the money the ambassadors you sign up earn.

In each offer I want a learn more button .

Industry/Entity Type

Business

Font styles to use
Serif

```html
<!DOCTYPE html>
<html lang="en">
<head>
<meta charset="utf-8">
<title>Tarnwickhub.com – Home</title>
<link href="https://fonts.googleapis.com/css2?family=Roboto+Condensed:ital,wght@0,300;0,400;0,700;1,700&family=Roboto:wght@400&display=swap" rel="stylesheet">
<style>
  :root {
    --page-bg: #f4f7fc;
    --header-bg: #ffffff;
    --brand-green: #2aae5b;
    --nav-text: #555a60;
    --offer-blue: #2786e3;
    --offer-green: #2aae5b;
    --offer-dark: #222222;
    --button-bg: #111111;
    --white: #ffffff;
    --shadow: rgba(0, 0, 0, 0.85);
    --logo-grey: #6e7378;
  }
  * { box-sizing: border-box; margin: 0; padding: 0; }
  html, body {
    width: 1200px;
    height: 631px;
    overflow: hidden;
    background: var(--page-bg);
  }
  .page {
    position: relative;
    width: 1200px;
    height: 631px;
    background: var(--page-bg);
    font-family: "Roboto Condensed", "Arial Narrow", sans-serif;
  }
  .site-header {
    position: absolute;
    left: 0; top: 0;
    width: 1200px;
    height: 78px;
    background: var(--header-bg);
  }
  .brand {
    position: absolute;
    left: 6px;
    top: 14px;
    font-family: "Roboto Condensed", sans-serif;
    font-weight: 700;
    font-size: 40px;
    line-height: 44px;
    color: var(--brand-green);
    letter-spacing: -0.5px;
  }
  .main-nav {
    position: absolute;
    right: 30px;
    top: 0;
    height: 78px;
    display: flex;
    font-family: "Roboto", sans-serif;
    font-size: 15px;
  }
  .main-nav a {
    display: flex;
    align-items: center;
    height: 78px;
    padding: 0 16px;
    color: var(--nav-text);
    text-decoration: none;
  }
  .main-nav a.is-active {
    background: var(--brand-green);
    color: var(--white);
    width: 72px;
    justify-content: center;
    margin-right: 0;
  }
  .offer {
    position: absolute;
    left: 32px;
    width: 836px;
    border-radius: 4px;
    color: var(--white);
    padding: 10px 14px 0 15px;
  }
  .offer::after {
    content: "";
    position: absolute;
    left: 18px;
    right: 30px;
    bottom: -12px;
    height: 12px;
    background: var(--shadow);
    filter: blur(3px);
    z-index: -1;
  }
  .offer--advertiser { top: 107px; height: 131px; background: var(--offer-blue); }
  .offer--business   { top: 261px; height: 171px; background: var(--offer-green); }
  .offer--ambassador { top: 460px; height: 131px; background: var(--offer-dark); }
  .offer-title {
    font-weight: 700;
    font-size: 31px;
    line-height: 35px;
    text-transform: uppercase;
    letter-spacing: 0.1px;
  }
  .offer-text {
    font-weight: 300;
    font-size: 21px;
    line-height: 30px;
  }
  .learn-more {
    display: inline-block;
    margin-top: 6px;
    margin-left: 2px;
    padding: 0 12px;
    height: 36px;
    line-height: 36px;
    background: var(--button-bg);
    color: var(--white);
    font-weight: 700;
    font-style: italic;
    font-size: 17px;
    border-radius: 3px;
    text-decoration: none;
    box-shadow: 0 2px 3px rgba(0,0,0,0.35);
  }
  .offer--business .learn-more { margin-left: 6px; margin-top: 10px; }
  .presenter-photo {
    position: absolute;
    left: 895px;
    top: 130px;
    width: 305px;
    height: 501px;
    border-radius: 140px 140px 0 0;
    background: linear-gradient(180deg, #8a5c45 0%, #b58d78 30%, #7f8794 60%, #6a7280 100%);
  }
</style>
</head>
<body>
<div class="page">
  <header class="site-header">
    <div class="brand">Tarnwickhub</div>
    <nav class="main-nav">
      <a class="is-active" href="#">Home</a>
      <a href="#">How It Works</a>
      <a href="#">Search</a>
      <a href="#">Members</a>
      <a href="#">Log In</a>
    </nav>
  </header>

  <section class="offer offer--advertiser">
    <h2 class="offer-title">"Make a referral to existing advertiser"</h2>
    <p class="offer-text">Earn up to $5000 when you make a successful referral to one of our advertisers.</p>
    <a class="learn-more" href="#">Learn more</a>
  </section>

  <section class="offer offer--business">
    <h2 class="offer-title">"Sign up a new business to offer referral commisions to ambassaadors"</h2>
    <p class="offer-text">Earn up to $5000 or more when you earn 5% of money paid out by business in referral fees.</p>
    <a class="learn-more" href="#">Learn more</a>
  </section>

  <section class="offer offer--ambassador">
    <h2 class="offer-title">"Sign up new ambassadors"</h2>
    <p class="offer-text">Earn up to $5000 or more when you earn 5% of the money the ambassadors you sign up earn.</p>
    <a class="learn-more" href="#">Learn more</a>
  </section>

  <div class="presenter-photo" role="img" aria-label="Photo of a smiling businesswoman in a grey suit with arms crossed"></div>
</div>
</body>
</html>
```